Disability provider requiring digital flyer to promote services

My company works within the Disability sector (QCWP registered provider), currently operating in Sydney, Australia.
I require a digital brochure which lists our services and gives potential customers a quick look into what we do with a single glance.
Undecided whether this digital flyer is to be single or double sided, happy to consult with an experienced designer in this regard.
I prefer minimalist designs (which may be an issue for someone trying to convey information, I'm not sure), and possibly someone who can work with out watercolor logo.
Services include:
-Supported Independent Living
-Specialist Disability Accommodation
-Individualised Living Options Stage 1 & 2
-Home Modifications
-Occupational Therapy
-Support Coordination Levels 1 & 2
-Short Term Accommodation - STA Respite
-Drop In Supports
-Community Access

```html
<!DOCTYPE html>
<html lang="en">
<head>
<meta charset="utf-8">
<title>Clearpath Care – Services Flyer</title>
<link href="https://fonts.googleapis.com/css2?family=Montserrat:wght@400;500;600;700&display=swap" rel="stylesheet">
<style>
  :root{
    --teal:#3fbb9b;
    --teal-dark:#2fa486;
    --ink:#1c1c1c;
    --paper:#ffffff;
    --soft:#f4f5f4;
    --stage:#a9a9a9;
    --text-dark:#2a2a2a;
    --photo-light:#d9ead0;
    --photo-mid:#8fbf6a;
    --photo-deep:#4f7f3a;
    --c-purple:#6b56b0;
    --c-orange:#f06a45;
    --c-pink:#e4348a;
    --c-blue:#35a6e6;
    --c-violet:#7a5bc2;
    --c-sky:#3a9fe0;
  }
  *{box-sizing:border-box;margin:0;padding:0}
  html,body{width:1200px;height:2316px;overflow:hidden}
  body{background:var(--stage);font-family:'Montserrat',sans-serif;position:relative}
  .flyer{
    position:absolute;left:60px;top:394px;width:875px;height:1238px;
    transform:scale(1.2343);transform-origin:0 0;
    background:var(--paper);overflow:hidden;
    box-shadow:0 6px 20px rgba(0,0,0,.25);
  }
  .backdrop{position:absolute;inset:0}
  .hero-photo{position:absolute;left:0;top:0;width:875px;height:520px;
    background:linear-gradient(135deg,var(--photo-light) 0%,var(--photo-mid) 45%,var(--photo-deep) 100%)}
  .brand{position:absolute;left:26px;top:170px;display:flex;align-items:center;gap:10px;
    font-weight:600;font-size:30px;color:var(--ink);letter-spacing:.5px}
  .brand-dot{width:18px;height:18px;border-radius:50%;background:var(--teal)}
  .portrait{position:absolute;border-radius:50%;border:7px solid var(--teal);
    box-shadow:0 0 0 3px var(--paper) inset;
    background:radial-gradient(circle at 40% 35%,#e6efe0,#9cc27c 60%,#6b9552)}
  .p1{left:146px;top:380px;width:170px;height:170px}
  .p2{left:330px;top:323px;width:210px;height:210px;background:radial-gradient(circle at 50% 40%,#eef2f0,#b9cfc2 60%,#7d9a88)}
  .p3{left:560px;top:381px;width:170px;height:170px;background:radial-gradient(circle at 45% 35%,#f5eecf,#d9c28a 55%,#8c7a60)}
  .about{position:absolute;left:0;top:560px;width:875px;text-align:center;color:var(--paper)}
  .about h2{font-size:29px;font-weight:700;letter-spacing:.5px}
  .about .rule{width:345px;height:2px;background:var(--teal);margin:6px auto 10px}
  .about p{font-size:14.2px;line-height:17.5px;letter-spacing:.6px;padding:0 28px;margin-bottom:8px}
  .services-title{position:absolute;left:0;top:808px;width:875px;height:52px}
  .services-title .line{position:absolute;left:25px;right:25px;top:26px;height:2px;background:var(--teal)}
  .services-title h2{position:absolute;left:295px;width:285px;top:0;height:52px;border:2px solid var(--teal);
    border-radius:26px;background:var(--paper);text-align:center;line-height:48px;
    font-size:29px;font-weight:700;color:var(--ink);letter-spacing:.5px}
  .services{position:absolute;left:25px;top:872px;width:823px;display:grid;
    grid-template-columns:repeat(3,268px);column-gap:10px;row-gap:12px;list-style:none}
  .service{height:66px;border-radius:33px;background:var(--paper);display:flex;align-items:center;gap:12px;padding-left:6px;
    box-shadow:0 2px 6px rgba(0,0,0,.12);font-size:14.5px;font-weight:600;line-height:16px;color:var(--text-dark);letter-spacing:.4px}
  .icon{width:54px;height:54px;border-radius:50%;flex:none;display:flex;align-items:center;justify-content:center}
  .icon svg{width:30px;height:30px;fill:none;stroke:#fff;stroke-width:1.6;stroke-linecap:round;stroke-linejoin:round}
  .i-purple{background:var(--c-purple)} .i-orange{background:var(--c-orange)} .i-pink{background:var(--c-pink)}
  .i-teal{background:var(--teal)} .i-violet{background:var(--c-violet)} .i-blue{background:var(--c-sky)}
  .contact{position:absolute;left:25px;top:1123px;width:823px;height:88px}
  .contact-web{position:absolute;left:400px;top:0;width:423px;height:88px;border-radius:44px;background:var(--ink);
    padding-left:110px;display:flex;flex-direction:column;justify-content:center;gap:12px;color:#fff;font-size:15.5px;letter-spacing:.6px}
  .contact-web div{display:flex;align-items:center;gap:12px}
  .contact-web b{color:var(--teal);font-weight:600}
  .mini{width:22px;height:22px;border-radius:50%;background:var(--teal);display:flex;align-items:center;justify-content:center;flex:none}
  .mini svg{width:13px;height:13px;fill:none;stroke:#fff;stroke-width:1.8}
  .contact-main{position:absolute;left:0;top:0;width:462px;height:88px;border-radius:44px;background:var(--teal);
    box-shadow:0 0 0 6px var(--paper)}
  .contact-main .label{position:absolute;left:22px;top:0;line-height:88px;font-size:20px;font-weight:600;color:#fff;letter-spacing:.8px}
  .phone{position:absolute;left:166px;top:10px;width:284px;height:68px;border-radius:34px;background:var(--paper);
    display:flex;align-items:center;gap:12px;padding-left:10px;font-size:21.5px;font-weight:700;color:var(--ink);letter-spacing:.3px}
  .phone .ring{width:48px;height:48px;border-radius:50%;border:3px solid var(--teal);display:flex;align-items:center;justify-content:center}
  .phone svg{width:24px;height:24px;fill:none;stroke:var(--teal);stroke-width:2}
</style>
</head>
<body>
<main class="flyer">
  <svg class="backdrop" width="875" height="1238" viewBox="0 0 875 1238">
    <rect width="875" height="1238" fill="#f6f7f6"/>
  </svg>
  <div class="hero-photo" role="img" aria-label="Photo of a smiling carer with an older woman in a wheelchair in a sunny park"></div>
  <svg class="backdrop" width="875" height="1238" viewBox="0 0 875 1238">
    <path d="M600 470 C700 420 800 400 875 395 L875 440 C780 445 690 470 600 500 Z" fill="var(--teal)" opacity=".8"/>
    <path d="M0 440 C220 405 560 500 875 420 L875 820 C600 770 260 770 0 830 Z" fill="var(--ink)"/>
    <path d="M0 818 C260 760 600 755 875 800 L875 812 C600 772 260 782 0 838 Z" fill="var(--teal)"/>
    <path d="M0 838 C260 782 600 772 875 812 L875 1238 L0 1238 Z" fill="#f6f7f6"/>
  </svg>

  <div class="brand"><span class="brand-dot"></span>Clearpath Care</div>

  <div class="portrait p1" role="img" aria-label="Photo of a couple outdoors, one seated in a wheelchair"></div>
  <div class="portrait p2" role="img" aria-label="Photo of a family with an elderly relative in a wheelchair"></div>
  <div class="portrait p3" role="img" aria-label="Photo of a support worker helping a child at a table"></div>

  <section class="about">
    <h2>About Us</h2>
    <div class="rule"></div>
    <p>Clearpath Care is a Sydney based disability support services provider. Focusing on intel-<br>lectual, physical &amp; sensory disabilities including mental health within the greater Sydney region,<br>we strive to assist our participants in leading an independent and fulfilling life.</p>
    <p>At Clearpath Care we aim to improve the lives of Participants who have been affected<br>with disability by providing services which best promote the continuation of daily life within the<br>immediate &amp; greater community.</p>
  </section>

  <div class="services-title"><div class="line"></div><h2>Our Services</h2></div>

  <ul class="services">
    <li class="service"><span class="icon i-purple"><svg viewBox="0 0 30 30"><path d="M6 25V12l9-6 9 6v13Z"/><path d="M12 25v-7h6v7"/></svg></span>Supported<br>Independent Living</li>
    <li class="service"><span class="icon i-orange"><svg viewBox="0 0 30 30"><path d="M5 14 15 6l10 8"/><path d="M8 12v13h14V12"/><path d="M13 19h4"/></svg></span>Home<br>Modifications</li>
    <li class="service"><span class="icon i-pink"><svg viewBox="0 0 30 30"><path d="M5 14 15 6l10 8"/><path d="M8 12v13h14V12"/><rect x="12" y="17" width="6" height="8"/></svg></span>Short Term<br>Accommodation-<br>STA Respite</li>
    <li class="service"><span class="icon i-pink"><svg viewBox="0 0 30 30"><path d="M5 14 15 6l10 8"/><path d="M8 12v13h14V12"/><circle cx="15" cy="19" r="3"/></svg></span>Specialist Disability<br>Accommodation</li>
    <li class="service"><span class="icon i-teal"><svg viewBox="0 0 30 30"><rect x="7" y="8" width="6" height="16"/><rect x="17" y="8" width="6" height="16"/><path d="M5 24h20"/></svg></span>Occupational<br>Therapy</li>
    <li class="service"><span class="icon i-violet"><svg viewBox="0 0 30 30"><circle cx="15" cy="15" r="3"/><circle cx="8" cy="8" r="2.5"/><circle cx="22" cy="8" r="2.5"/><circle cx="8" cy="22" r="2.5"/><circle cx="22" cy="22" r="2.5"/><path d="M10 10l3 3M20 10l-3 3M10 20l3-3M20 20l-3-3"/></svg></span>Drop In<br>Supports</li>
    <li class="service"><span class="icon i-blue"><svg viewBox="0 0 30 30"><rect x="6" y="12" width="18" height="10" rx="2"/><path d="M10 12V9h10v3M6 22v3M24 22v3"/></svg></span>Individualised Living<br>Options Stage 1 &amp; 2</li>
    <li class="service"><span class="icon i-orange"><svg viewBox="0 0 30 30"><path d="M15 24 6 15a5 5 0 0 1 9-5 5 5 0 0 1 9 5Z"/></svg></span>Support Coordination<br>Levels 1 &amp; 2</li>
    <li class="service"><span class="icon i-blue"><svg viewBox="0 0 30 30"><circle cx="15" cy="10" r="3"/><circle cx="8" cy="17" r="2.5"/><circle cx="22" cy="17" r="2.5"/><path d="M10 24a5 5 0 0 1 10 0M4 24a4 4 0 0 1 8 0M18 24a4 4 0 0 1 8 0"/></svg></span>Community<br>Access</li>
  </ul>

  <div class="contact">
    <div class="contact-web">
      <div><span class="mini"><svg viewBox="0 0 14 14"><rect x="1.5" y="3" width="11" height="8"/><path d="M1.5 3 7 8l5.5-5"/></svg></span>info@<b>clearpathcare</b>.com.au</div>
      <div><span class="mini"><svg viewBox="0 0 14 14"><circle cx="7" cy="7" r="5.5"/><path d="M1.5 7h11M7 1.5c2.5 3 2.5 8 0 11M7 1.5c-2.5 3-2.5 8 0 11"/></svg></span>www.<b>clearpathcare</b>.com.au</div>
    </div>
    <div class="contact-main">
      <span class="label">Contact Us</span>
      <div class="phone"><span class="ring"><svg viewBox="0 0 24 24"><path d="M6 3h3l2 5-2.5 1.5a11 11 0 0 0 6 6L16 13l5 2v3a2 2 0 0 1-2 2A16 16 0 0 1 4 5a2 2 0 0 1 2-2Z"/></svg></span>+61 0400 123 456</div>
    </div>
  </div>
</main>
</body>
</html>
```